Urine collection cup with and without sterile seal sticker

Hello. We need a urine cup label designed please with

Name:
Date of Birth:
Date:
Time:
Temp℃:
Specimen ID:

Product code: TUB-47
Volume markings (e.g., 30 mL, 60 mL, 90 mL).
Vela Drug Tests logo

Could you please provide one version with the additional sterile sticker extending to the top, and one version without the additional sterile sticker?

```html
<!DOCTYPE html>
<html lang="en">
<head>
<meta charset="utf-8">
<title>Vela Drug Tests – Collection Cup Labels</title>
<link rel="stylesheet" href="https://fonts.googleapis.com/css2?family=Montserrat:wght@500;700;800&display=swap">
<style>
  :root {
    --brand: #27a1e4;
    --backdrop: #b3b3b3;
    --card: #ffffff;
    --ink: #1e1e1e;
    --muted: #f2f2f2;
  }
  html, body {
    margin: 0;
    padding: 0;
    width: 1200px;
    height: 3240px;
    overflow: hidden;
    background: var(--card);
    font-family: 'Montserrat', sans-serif;
  }
  .board {
    position: absolute;
    left: 0; top: 0;
    width: 1200px;
    height: 2476px;
    background: var(--backdrop);
  }
  .swatch {
    position: absolute;
    left: 887px; top: 154px;
    width: 128px; height: 128px;
    border-radius: 50%;
    background: var(--brand);
  }
  .swatch-caption {
    position: absolute;
    left: 801px; top: 330px;
    width: 300px;
    text-align: center;
    color: var(--muted);
    font-size: 35px;
    font-weight: 500;
    line-height: 55px;
  }
  .label {
    position: absolute;
    width: 905px;
    height: 918px;
    overflow: visible;
  }
  .label--nonsterile { left: 158px; top: 309px; }
  .label--sterile { left: 140px; top: 1320px; }
  .tab { fill: var(--brand); }
  .tab-rule { stroke: #fff; stroke-width: 4; }
  .seal-note { fill: #fff; font-weight: 700; font-size: 20px; letter-spacing: 0.5px; }
  .seal-word { fill: #fff; font-weight: 800; font-size: 44px; letter-spacing: 16px; }
  .card { fill: var(--card); }
  .field { fill: var(--ink); font-weight: 500; font-size: 35px; }
  .rule { stroke: var(--ink); stroke-width: 2.5; }
  .box { fill: none; stroke: var(--ink); stroke-width: 2.5; }
  .brand-dot { fill: var(--brand); }
  .brand-name { fill: var(--ink); font-weight: 700; font-size: 44px; }
  .mockup {
    position: absolute;
    left: 0; top: 2476px;
    width: 1200px; height: 764px;
    background: linear-gradient(180deg, #ffffff 0%, #eef6fb 55%, #ffffff 100%);
  }
</style>
</head>
<body>
<main class="board">
  <div class="swatch"></div>
  <div class="swatch-caption">Brand Color<br>#27a1e4</div>

  <svg class="label label--nonsterile" viewBox="0 0 905 918" xmlns="http://www.w3.org/2000/svg">
    <path class="tab" d="M0 918 V63 A63 63 0 0 1 126 63 V918 Z"/>
    <line class="tab-rule" x1="26" y1="311" x2="26" y2="918"/>
    <line class="tab-rule" x1="104" y1="311" x2="104" y2="918"/>
    <g transform="rotate(-90)">
      <text class="seal-note" x="-292" y="38">INTERIOR</text>
      <text class="seal-note" x="-292" y="70">AS LONG AS SEAL</text>
      <text class="seal-note" x="-292" y="102">REAMAINS INTACT</text>
      <text class="seal-word" x="-625" y="82" text-anchor="middle">NONSTERILE</text>
    </g>
    <path class="card" d="M126 270 H873 A28 28 0 0 1 901 298 V890 A28 28 0 0 1 873 918 H126 Z"/>
    <g class="fields">
      <text class="field" x="169" y="345">Name:</text><line class="rule" x1="295" y1="353" x2="855" y2="353"/>
      <text class="field" x="169" y="400">Date of Birth:</text><line class="rule" x1="417" y1="408" x2="855" y2="408"/>
      <text class="field" x="169" y="455">Date:</text><line class="rule" x1="276" y1="463" x2="855" y2="463"/>
      <text class="field" x="169" y="510">Time:</text><line class="rule" x1="276" y1="518" x2="855" y2="518"/>
      <text class="field" x="169" y="565">Temp:</text><line class="rule" x1="289" y1="573" x2="855" y2="573"/>
      <text class="field" x="169" y="620">Specimen ID:</text><line class="rule" x1="421" y1="628" x2="855" y2="628"/>
      <text class="field" x="169" y="729">Product code: TUB-47</text>
      <text class="field" x="169" y="783">Volume:</text>
      <rect class="box" x="348" y="753" width="33" height="33" rx="5"/><text class="field" x="384" y="783">30 mL</text>
      <rect class="box" x="520" y="753" width="33" height="33" rx="5"/><text class="field" x="556" y="783">60 mL</text>
      <rect class="box" x="691" y="753" width="33" height="33" rx="5"/><text class="field" x="727" y="783">90 mL</text>
    </g>
    <circle class="brand-dot" cx="200" cy="853" r="31"/>
    <text class="brand-name" x="244" y="868">Vela Drug Tests</text>
  </svg>

  <svg class="label label--sterile" viewBox="0 0 905 918" xmlns="http://www.w3.org/2000/svg">
    <path class="tab" d="M0 918 V63 A63 63 0 0 1 126 63 V918 Z"/>
    <line class="tab-rule" x1="26" y1="311" x2="26" y2="918"/>
    <line class="tab-rule" x1="104" y1="311" x2="104" y2="918"/>
    <g transform="rotate(-90)">
      <text class="seal-note" x="-292" y="38">INTERIOR</text>
      <text class="seal-note" x="-292" y="70">AS LONG AS SEAL</text>
      <text class="seal-note" x="-292" y="102">REAMAINS INTACT</text>
      <text class="seal-word" x="-625" y="82" text-anchor="middle" style="letter-spacing:30px">STERILE</text>
    </g>
    <path class="card" d="M126 270 H873 A28 28 0 0 1 901 298 V890 A28 28 0 0 1 873 918 H126 Z"/>
    <g class="fields">
      <text class="field" x="169" y="345">Name:</text><line class="rule" x1="295" y1="353" x2="855" y2="353"/>
      <text class="field" x="169" y="400">Date of Birth:</text><line class="rule" x1="417" y1="408" x2="855" y2="408"/>
      <text class="field" x="169" y="455">Date:</text><line class="rule" x1="276" y1="463" x2="855" y2="463"/>
      <text class="field" x="169" y="510">Time:</text><line class="rule" x1="276" y1="518" x2="855" y2="518"/>
      <text class="field" x="169" y="565">Temp:</text><line class="rule" x1="289" y1="573" x2="855" y2="573"/>
      <text class="field" x="169" y="620">Specimen ID:</text><line class="rule" x1="421" y1="628" x2="855" y2="628"/>
      <text class="field" x="169" y="729">Product code: TUB-47</text>
      <text class="field" x="169" y="783">Volume:</text>
      <rect class="box" x="348" y="753" width="33" height="33" rx="5"/><text class="field" x="384" y="783">30 mL</text>
      <rect class="box" x="520" y="753" width="33" height="33" rx="5"/><text class="field" x="556" y="783">60 mL</text>
      <rect class="box" x="691" y="753" width="33" height="33" rx="5"/><text class="field" x="727" y="783">90 mL</text>
    </g>
    <circle class="brand-dot" cx="200" cy="853" r="31"/>
    <text class="brand-name" x="244" y="868">Vela Drug Tests</text>
  </svg>
</main>

<div class="mockup" role="img" aria-label="Product mockup: two labelled specimen collection cups with blue lids, front and back views"></div>
</body>
</html>
```